FeedBack Solution Provider - Web Redesign

Tolvera Website design request We are looking for a redesign for our website www.tolvera-demo.net 1 web page site +2, we are providing feedback collection solution through tablet devices and online iframes, sms, emails.. we want to optimize our website design to communicate our products values better (increase your customer satisfaction – get to know your customers – happy customers – increased business performance)Also to give visitors more insight to our different products (channels) layouts.A pricing section for minimum of 2 packages (SAAS) that include many features and hardware addons as a selection field. 3rd package clients to design their own packages through selection of components and addons no price needed in this feature (request quote).1 Web Page Sections will go as follows:1. Header2. Slider3. Why TolVera (points and values)4. Features 5. Packages (pricing based on SaaS and hardware as addon)6. Impact of using RaiBack7. Clients Testimonies8. Contact9. Footer +2 Web Pages Adding to additional web pages by copying the following sections with different content (will be hidden for the moment)1. Slider2. Features 3. Packages (pricing based on SaaS and hardware as addon)4. Impact of using RaiBack5. Clients TestimoniesHints: https://pelunor42.examplesite.net/tolvera www.tolvera-demo.net

Target Market(s)

B2B

Industry/Entity Type

SaaS

Number of Pages Required

1 page

Font styles to use
Sans Serif

Colors

Designer to choose colors to be used in the design.

Requirements
Must have
• 1 Web Page Sections will go as follows:
• 1. Header
• 2. Slider
• 3. Why TolVera (points and values)
• 4. Features
• 5. Packages (pricing based on SaaS and hardware as addon)
• 6. Impact of using TolVera
• 7. Clients Testimonies
• 8. Contact
• 9. Footer
Nice to have
• +2 Web Pages Adding to additional web pages by copying the following sections with different content (will be hidden for the moment)
• 1. Slider
• 2. Features
• 3. Packages (pricing based on SaaS and hardware as addon)
• 4. Impact of using TolVera
• 5. Clients Testimonies

```html
<!DOCTYPE html>
<html lang="en">
<head>
<meta charset="utf-8">
<title>Tolvera – Packages</title>
<link href="https://fonts.googleapis.com/css2?family=Montserrat:wght@300;400;500&display=swap" rel="stylesheet">
<style>
:root{
  --blue:#3db4f9;
  --orange:#fca63c;
  --dark:#41474f;
  --page:#f4f7fa;
  --white:#ffffff;
  --text:#3f4650;
  --muted:#8c95a0;
  --line:#e3e8ee;
}
*{margin:0;padding:0;box-sizing:border-box}
html,body{width:1200px;height:1183px;overflow:hidden}
body{font-family:'Montserrat',sans-serif;background:var(--page);color:var(--text)}
.quote-band{height:254px;background:var(--blue);color:var(--white);text-align:center;padding-top:36px}
.quote-band h1{font-weight:300;font-size:36px;line-height:1;letter-spacing:.3px}
.quote-band p{font-size:13.3px;line-height:20px;width:720px;margin:21px auto 0}
.btn-quote{display:inline-block;margin-top:20px;width:242px;height:52px;line-height:52px;background:var(--orange);color:var(--white);font-size:15px;font-weight:500;text-decoration:none}
.packages{text-align:center;padding-top:97px}
.packages h2{font-weight:300;font-size:30px;line-height:32px}
.billing-toggle{display:flex;justify-content:center;margin-top:50px}
.billing-toggle span{height:34px;line-height:34px;font-size:12.5px;font-weight:500;color:var(--white);letter-spacing:.3px}
.billing-toggle .monthly{width:153px;background:var(--blue)}
.billing-toggle .annual{width:155px;background:var(--dark)}
.save-note{font-size:13px;margin-top:12px}
.plans{position:relative;margin-top:55px;height:477px}
.plan{position:absolute;top:0;width:293px;height:477px;background:var(--white);border:1px solid var(--line);border-radius:7px;overflow:hidden}
.plan.personal{left:124px}
.plan.standard{left:454px}
.plan.custom{left:782px}
.plan-head{height:206px;padding-top:28px}
.standard .plan-head{background:var(--blue);color:var(--white)}
.custom .plan-head{background:var(--dark);color:var(--white)}
.plan-name{font-size:20px;font-weight:400;line-height:24px}
.plan-price{margin-top:22px;font-size:36px;font-weight:500;line-height:40px}
.plan-price small{font-size:12.5px;font-weight:400}
.plan-desc{font-size:12px;line-height:20px;width:240px;margin:7px auto 0}
.features{list-style:none;padding-top:11px;height:226px}
.features li{height:41px;line-height:41px;font-size:13px}
.features li.off{text-decoration:line-through;color:var(--muted)}
.options{padding:11px 48px 0 48px;height:226px;text-align:left}
.options .row{display:flex;justify-content:space-between;align-items:center;height:40px;font-size:13px}
.select{width:62px;height:27px;border:1px solid #d9dee4;background:var(--white);color:var(--muted);font-size:12.5px;display:flex;align-items:center;justify-content:flex-end;padding-right:7px;gap:10px}
.btn{display:inline-block;width:95px;height:32px;line-height:31px;border-radius:16px;font-size:11.5px;font-weight:500;text-decoration:none}
.btn.outline{border:1px solid #b3b9c0;color:var(--muted)}
.btn.solid{background:var(--blue);color:var(--white)}
.btn.dark{width:144px;background:var(--dark);color:var(--white)}
</style>
</head>
<body>
<section class="quote-band">
  <h1>Get Quote Now</h1>
  <p>Lorem Ipsum is simply dummy text of the printing and typesetting industry. Lorem Ipsum has been the industry's standard dummy text ever since the took a galley.</p>
  <a class="btn-quote" href="#">Request Quote</a>
</section>

<section class="packages">
  <h2>Our packages</h2>
  <div class="billing-toggle"><span class="monthly">MONTHLY BASIS</span><span class="annual">ANNUAL BASIS</span></div>
  <p class="save-note">(Save up to 30% off on annual plans)</p>

  <div class="plans">
    <article class="plan personal">
      <div class="plan-head">
        <h3 class="plan-name">Personal</h3>
        <p class="plan-price">$9.99<small>/month</small></p>
        <p class="plan-desc">Includes simple but powerful functionality for individuals and small teams. You can upgrade on the way</p>
      </div>
      <ul class="features">
        <li class="off">Cras justo odio</li>
        <li class="off">Dapibus ac facilisis in</li>
        <li class="off">Morbi leo risus</li>
        <li>Porta ac consectetur ac</li>
        <li>Vestibulum at eros</li>
      </ul>
      <a class="btn outline" href="#">BUY NOW</a>
    </article>

    <article class="plan standard">
      <div class="plan-head">
        <h3 class="plan-name">Standard</h3>
        <p class="plan-price">$39.99<small>/month</small></p>
        <p class="plan-desc">Includes simple but powerful functionality for individuals and small teams. You can upgrade on the way</p>
      </div>
      <ul class="features">
        <li class="off">Cras justo odio</li>
        <li>Dapibus ac facilisis in</li>
        <li>Morbi leo risus</li>
        <li>Porta ac consectetur ac</li>
        <li>Vestibulum at eros</li>
      </ul>
      <a class="btn solid" href="#">BUY NOW</a>
    </article>

    <article class="plan custom">
      <div class="plan-head">
        <h3 class="plan-name">Custom Package</h3>
        <p class="plan-price">$1,234<small>/month</small></p>
        <p class="plan-desc">Includes simple but powerful functionality for individuals and small teams. You can upgrade on the way</p>
      </div>
      <div class="options">
        <div class="row"><span>Number of Sites</span><span class="select">5<svg width="5" height="9" viewBox="0 0 5 9"><path d="M2.5 0L5 3.5H0zM2.5 9L0 5.5h5z" fill="#8c95a0"/></svg></span></div>
        <div class="row"><span>Email</span><span class="select">100k<svg width="5" height="9" viewBox="0 0 5 9"><path d="M2.5 0L5 3.5H0zM2.5 9L0 5.5h5z" fill="#8c95a0"/></svg></span></div>
        <div class="row"><span>Social Media</span><span class="select">4<svg width="5" height="9" viewBox="0 0 5 9"><path d="M2.5 0L5 3.5H0zM2.5 9L0 5.5h5z" fill="#8c95a0"/></svg></span></div>
        <div class="row"><span>Iframes</span><span class="select">15<svg width="5" height="9" viewBox="0 0 5 9"><path d="M2.5 0L5 3.5H0zM2.5 9L0 5.5h5z" fill="#8c95a0"/></svg></span></div>
        <div class="row"><span>SMS</span><span class="select">10k<svg width="5" height="9" viewBox="0 0 5 9"><path d="M2.5 0L5 3.5H0zM2.5 9L0 5.5h5z" fill="#8c95a0"/></svg></span></div>
      </div>
      <div style="text-align:center"><a class="btn dark" href="#">REQUEST A QUOTE</a></div>
    </article>
  </div>
</section>
</body>
</html>
```